Sir Sparkline Auto Electrical, mobile auto auto electrician

I have a dual cab ute that i use for work im looking to get sign written up. Im an mobile auto electrician that is looking for a stand out modern style design that will catch the attention of customers on the road while travelling between jobs. Would like it to have 4x4 inspiration design as that the market im targeting. Would like to have dot points of what type of work i do , 4x4 touring and off grid 12v installation and diagnostics. Have my phone number 0418 356 274

Target Market(s)

4x4 touring and cravan market

Industry/Entity Type

Automotive 12 volt

Font styles to use
Script

Colors

Designer to choose colors to be used in the design.

Requirements
Must have
• Logo, phone number, stating that im mobile, company name offgrid, 4x4 touring, diagnostics
Nice to have
• Would be good to have some form of off road inspiration

```html
<!DOCTYPE html>
<html lang="en">
<head>
<meta charset="utf-8">
<title>Sir Sparkline Auto Electrical – Ute Wrap</title>
<link rel="stylesheet" href="https://fonts.googleapis.com/css2?family=Montserrat:ital,wght@0,700;1,700&family=Oswald:wght@500&family=Poppins:wght@500&display=swap">
<style>
  :root {
    --bg: #2e2e30;
    --body-white: #efece6;
    --wrap-brown: #8d623f;
    --tread-brown: #5e3e25;
    --mud-light: #a0764f;
    --ink-black: #1d1d1f;
    --text-white: #ffffff;
    --logo-brown: #7a5334;
    --faint: #d6cfc3;
  }
  html, body { margin: 0; padding: 0; overflow: hidden; }
  body {
    width: 1200px; height: 3373px;
    background: var(--bg);
    display: flex; flex-direction: column;
  }
  .view {
    height: 674.6px;
    display: flex; align-items: center; justify-content: center;
    border-bottom: 1px solid #262628;
  }
  .view svg { display: block; }
  .phone { font-family: "Montserrat", sans-serif; font-weight: 700; font-style: italic; fill: var(--text-white); }
  .services { font-family: "Oswald", sans-serif; font-weight: 500; fill: var(--text-white); }
  .tagline { font-family: "Poppins", sans-serif; font-weight: 500; fill: var(--text-white); }
  .brand-name { font-family: "Montserrat", sans-serif; font-weight: 700; fill: var(--logo-brown); }
  .brand-name--light { fill: var(--body-white); }
  .brand-name--faint { fill: var(--faint); }
</style>
</head>
<body>
<svg width="0" height="0" style="position:absolute">
  <defs>
    <linearGradient id="mudSwathRight" x1="0" y1="1" x2="1" y2="0">
      <stop offset="0" stop-color="var(--tread-brown)" stop-opacity="0.95"/>
      <stop offset="0.55" stop-color="var(--tread-brown)" stop-opacity="0.75"/>
      <stop offset="1" stop-color="var(--wrap-brown)" stop-opacity="0.4"/>
    </linearGradient>
    <linearGradient id="mudSwathLeft" x1="1" y1="1" x2="0" y2="0">
      <stop offset="0" stop-color="var(--tread-brown)" stop-opacity="0.95"/>
      <stop offset="0.55" stop-color="var(--tread-brown)" stop-opacity="0.75"/>
      <stop offset="1" stop-color="var(--wrap-brown)" stop-opacity="0.4"/>
    </linearGradient>
    <radialGradient id="mudArc" cx="0.7" cy="0.9" r="0.8">
      <stop offset="0" stop-color="var(--tread-brown)" stop-opacity="0.9"/>
      <stop offset="1" stop-color="var(--wrap-brown)" stop-opacity="0"/>
    </radialGradient>
  </defs>
</svg>

<!-- Driver side panel -->
<section class="view view--driver-side">
  <svg width="1100" height="380" viewBox="0 0 1100 380">
    <path d="M20 130 Q30 80 90 72 L300 60 L1080 60 L1080 300 L930 300 Q920 210 840 210 Q760 210 750 300 L330 300 Q320 210 240 210 Q160 210 150 300 L20 300 Z" fill="var(--body-white)"/>
    <path d="M700 60 L1080 60 L1080 300 L930 300 Q920 210 840 210 Q760 210 750 300 L620 300 Z" fill="var(--wrap-brown)"/>
    <path role="img" aria-label="Mud splatter edge with tyre tread track sweeping up the rear door"
      d="M590 300 L612 262 L600 240 L628 210 L622 182 L650 160 L646 132 L676 112 L672 84 L700 60 L790 60 L770 110 L750 170 L722 240 L700 300 Z"
      fill="url(#mudSwathRight)"/>
    <path d="M940 300 Q980 248 1080 238 L1080 268 Q1000 275 965 300 Z" fill="var(--ink-black)"/>
    <rect x="660" y="78" width="400" height="56" rx="28" fill="var(--ink-black)"/>
    <text class="phone" x="860" y="119" font-size="36" text-anchor="middle">0418 356 274</text>
    <text class="services" x="860" y="168" font-size="21" text-anchor="middle">4X4 TOURING • DIAGNOSTICS • 12V FITOUT</text>
    <circle cx="420" cy="128" r="26" fill="var(--logo-brown)"/>
    <text class="brand-name" x="420" y="186" font-size="21" text-anchor="middle">Sir Sparkline</text>
    <text class="brand-name" x="420" y="208" font-size="14" text-anchor="middle">AUTO ELECTRICAL</text>
    <path d="M260 258 L610 258 L598 294 L260 294 Z" fill="var(--ink-black)"/>
    <text class="tagline" x="430" y="283" font-size="19" text-anchor="middle">Mobile Auto Electrician</text>
  </svg>
</section>

<!-- Passenger side panel -->
<section class="view view--passenger-side">
  <svg width="1100" height="380" viewBox="0 0 1100 380">
    <path d="M1080 130 Q1070 80 1010 72 L800 60 L20 60 L20 300 L170 300 Q180 210 260 210 Q340 210 350 300 L770 300 Q780 210 860 210 Q940 210 950 300 L1080 300 Z" fill="var(--body-white)"/>
    <path d="M400 60 L20 60 L20 300 L170 300 Q180 210 260 210 Q340 210 350 300 L480 300 Z" fill="var(--wrap-brown)"/>
    <path role="img" aria-label="Mud splatter edge with tyre tread track sweeping up the rear door"
      d="M510 300 L488 262 L500 240 L472 210 L478 182 L450 160 L454 132 L424 112 L428 84 L400 60 L310 60 L330 110 L350 170 L378 240 L400 300 Z"
      fill="url(#mudSwathLeft)"/>
    <path d="M160 300 Q120 248 20 238 L20 268 Q100 275 135 300 Z" fill="var(--ink-black)"/>
    <rect x="40" y="78" width="400" height="56" rx="28" fill="var(--ink-black)"/>
    <text class="phone" x="240" y="119" font-size="36" text-anchor="middle">0418 356 274</text>
    <text class="services" x="240" y="168" font-size="21" text-anchor="middle">4X4 TOURING • DIAGNOSTICS • 12V FITOUT</text>
    <circle cx="690" cy="128" r="26" fill="var(--logo-brown)"/>
    <text class="brand-name" x="690" y="186" font-size="21" text-anchor="middle">Sir Sparkline</text>
    <text class="brand-name" x="690" y="208" font-size="14" text-anchor="middle">AUTO ELECTRICAL</text>
    <path d="M502 258 L850 258 L850 294 L490 294 Z" fill="var(--ink-black)"/>
    <text class="tagline" x="672" y="283" font-size="19" text-anchor="middle">Mobile Auto Electrician</text>
  </svg>
</section>

<!-- Tailgate panel -->
<section class="view view--tailgate">
  <svg width="1000" height="360" viewBox="0 0 1000 360">
    <rect x="0" y="0" width="1000" height="300" rx="10" fill="var(--wrap-brown)"/>
    <path role="img" aria-label="Curved tyre tread track with mud splatter across the tailgate"
      d="M300 0 L1000 0 L1000 190 Q860 60 600 40 Q420 30 300 60 Z" fill="url(#mudArc)"/>
    <rect x="0" y="300" width="1000" height="40" fill="var(--body-white)"/>
    <circle cx="150" cy="110" r="40" fill="var(--body-white)"/>
    <text class="brand-name brand-name--light" x="150" y="192" font-size="22" text-anchor="middle">Sir Sparkline</text>
    <text class="brand-name brand-name--light" x="150" y="216" font-size="14" text-anchor="middle">AUTO ELECTRICAL</text>
    <rect x="300" y="110" width="690" height="90" rx="45" fill="var(--ink-black)"/>
    <text class="phone" x="645" y="174" font-size="60" text-anchor="middle">0418 356 274</text>
    <text class="services" x="645" y="256" font-size="32" text-anchor="middle">4X4 TOURING • DIAGNOSTICS • 12V FITOUT</text>
  </svg>
</section>

<!-- Rear bed side panel -->
<section class="view view--bed-side">
  <svg width="1000" height="300" viewBox="0 0 1000 300">
    <rect x="0" y="0" width="1000" height="230" fill="var(--wrap-brown)"/>
    <path role="img" aria-label="Mud splatter edge with tyre tread track near the rear door"
      d="M800 230 L822 196 L810 170 L840 140 L832 110 L862 84 L856 52 L886 30 L880 0 L1000 0 L1000 230 Z"
      fill="url(#mudSwathRight)"/>
    <path d="M0 230 L1000 230 L1000 300 Q700 220 0 290 Z" fill="var(--body-white)"/>
    <path d="M0 210 Q500 180 1000 200 L1000 230 Q500 210 0 240 Z" fill="var(--ink-black)"/>
    <rect x="60" y="30" width="720" height="86" rx="43" fill="var(--ink-black)"/>
    <text class="phone" x="420" y="92" font-size="58" text-anchor="middle">0418 356 274</text>
    <text class="services" x="420" y="170" font-size="36" text-anchor="middle">4X4 TOURING • DIAGNOSTICS • 12V FITOUT</text>
  </svg>
</section>

<!-- Bonnet panel -->
<section class="view view--bonnet">
  <svg width="900" height="360" viewBox="0 0 900 360">
    <path d="M60 20 L840 20 L880 340 L20 340 Z" fill="var(--body-white)"/>
    <circle cx="450" cy="130" r="46" fill="var(--faint)"/>
    <text class="brand-name brand-name--faint" x="450" y="228" font-size="40" text-anchor="middle">Sir Sparkline</text>
    <text class="brand-name brand-name--faint" x="450" y="262" font-size="20" text-anchor="middle">AUTO ELECTRICAL</text>
  </svg>
</section>

</body>
</html>
```